Cleaning Bochure for Different Services

We need to create preferably an A4 brochure for cleaning services so we are able to give to our customers upon meeting them. check out our website for more info. It is www.brightvaleservices.co.uk We need a page on;-Commercial Cleaning-Carpet Cleaning-Oven Cleaning with description and some imagery.

Target Market(s)

Commercial Cleaning Customers

Industry/Entity Type

Office Cleaning

Font styles to use
Sans Serif

Colors
33a6d7
aaaaaa

Requirements
Must have
• 4 pages each containing these services
• -Commercial Cleaning (most important)
• -Carpet Cleaning
• -Oven Cleaning
Nice to have
• Clean and smart looking design use some imagination and possibly go wild!
• Must be eye catching!

```html
<!DOCTYPE html>
<html lang="en">
<head>
<meta charset="utf-8">
<title>Brightvale – Commercial Cleaning Brochure</title>
<link rel="stylesheet" href="https://fonts.googleapis.com/css2?family=Open+Sans:ital,wght@0,400;0,600;0,700;1,400&display=swap">
<style>
  :root {
    --brand-blue: #33a6d7;
    --deep-blue: #1b6fb0;
    --light-blue: #8fd0ec;
    --brand-grey: #aaaaaa;
    --dark-grey: #6d6d6d;
    --text: #4a4a4a;
    --canvas: #e8e8e8;
    --paper: #ffffff;
  }
  * { box-sizing: border-box; margin: 0; padding: 0; }
  html, body { width: 1200px; height: 2233px; overflow: hidden; }
  body { background: var(--canvas); font-family: "Open Sans", Arial, sans-serif; color: var(--text); position: relative; }

  .sheet { position: absolute; display: flex; box-shadow: 0 14px 30px rgba(0,0,0,.18); }
  .sheet--cover { left: 360px; top: 40px; }
  .sheet--outer-spread { left: 120px; top: 770px; }
  .sheet--inner-spread { left: 120px; top: 1500px; }

  .page { position: relative; width: 480px; height: 679px; background: var(--paper); overflow: hidden; }
  .page + .page { border-left: 1px solid #e2e2e2; }
  .page-art { position: absolute; inset: 0; width: 480px; height: 679px; }

  .brand { position: absolute; display: flex; align-items: center; gap: 8px; color: var(--brand-blue); font-weight: 700; font-size: 32px; letter-spacing: -0.5px; }
  .brand-dot { width: 16px; height: 16px; border-radius: 50%; background: var(--brand-blue); }

  .cover-title { position: absolute; left: 0; right: 0; text-align: center; color: #fff; }
  .cover-title h1 { font-size: 23px; font-weight: 700; letter-spacing: .3px; }
  .cover-title p { font-size: 18px; margin-top: 2px; }

  .phone-pill { position: absolute; display: flex; align-items: center; gap: 8px; height: 30px; padding: 0 16px 0 5px; border-radius: 15px;
    background: linear-gradient(#9a9a9a, #7b7b7b); color: #fff; font-weight: 700; font-size: 16px; box-shadow: 0 1px 3px rgba(0,0,0,.25); }
  .phone-pill .phone-icon { width: 22px; height: 22px; border-radius: 50%; background: #fff; display: flex; align-items: center; justify-content: center; }

  .heading { position: absolute; color: var(--brand-blue); font-weight: 600; font-size: 21px; line-height: 1.15; }
  .subheading { display: block; font-size: 15px; font-weight: 400; color: var(--text); }
  .body-copy { position: absolute; font-size: 10.5px; line-height: 1.45; color: var(--text); }
  .body-copy p + p { margin-top: 7px; }

  .ticks { position: absolute; list-style: none; font-size: 12px; color: var(--text); }
  .ticks li { position: relative; padding-left: 22px; margin-bottom: 6px; }
  .ticks li::before { content: ""; position: absolute; left: 0; top: 1px; width: 13px; height: 13px; border: 1.5px solid var(--brand-blue); border-radius: 2px; }
  .ticks li::after { content: ""; position: absolute; left: 4px; top: 0; width: 5px; height: 10px; border: solid var(--deep-blue); border-width: 0 2.5px 2.5px 0; transform: rotate(40deg); }

  .call-to-action { position: absolute; font-style: italic; color: var(--brand-blue); font-size: 12px; }
  .footer-line { position: absolute; color: #fff; font-size: 11px; letter-spacing: .5px; }
  .social-row { position: absolute; display: flex; gap: 8px; }
  .social-row span { width: 16px; height: 16px; border-radius: 50%; border: 1.5px solid #fff; }
  .cert-badge { position: absolute; width: 64px; height: 44px; border-radius: 4px; background: #d8dde5; border: 2px solid #9aa6b8; }
  .before-after { position: absolute; width: 72px; height: 64px; border-radius: 8px; border: 3px solid #fff; box-shadow: 0 1px 4px rgba(0,0,0,.35);
    background: linear-gradient(160deg, #6d6d6d, #2e2e2e); }
</style>
</head>
<body>

<!-- Front cover, standalone -->
<div class="sheet sheet--cover">
  <section class="page page--front-cover">
    <svg class="page-art" viewBox="0 0 480 679" aria-hidden="false">
      <defs>
        <linearGradient id="officeTone" x1="0" y1="0" x2="0" y2="1"><stop offset="0" stop-color="#d3dde5"/><stop offset="1" stop-color="#7d8c99"/></linearGradient>
        <linearGradient id="bandBlue" x1="0" y1="0" x2="0" y2="1"><stop offset="0" stop-color="#33a6d7"/><stop offset="1" stop-color="#1b6fb0"/></linearGradient>
        <radialGradient id="thumbTone"><stop offset="0" stop-color="#efe7da"/><stop offset="1" stop-color="#a99f90"/></radialGradient>
      </defs>
      <path role="img" aria-label="Photo of a bright empty open-plan office with large windows" d="M0 90 L480 90 L480 420 Q240 470 0 400 Z" fill="url(#officeTone)"/>
      <path d="M0 400 Q240 470 480 420 L480 445 Q240 492 0 428 Z" fill="#fff"/>
      <path d="M0 462 Q240 418 480 442 L480 466 Q240 444 0 484 Z" fill="var(--light-blue)"/>
      <path d="M0 480 Q240 440 480 462 L480 679 L0 679 Z" fill="url(#bandBlue)"/>
      <g stroke="#fff" stroke-width="4">
        <circle role="img" aria-label="Photo of a mop on a floor" cx="150" cy="432" r="40" fill="url(#thumbTone)"/>
        <circle role="img" aria-label="Photo of a carpet being steam cleaned" cx="240" cy="420" r="50" fill="url(#thumbTone)"/>
        <circle role="img" aria-label="Photo of a gloved hand wiping a surface" cx="330" cy="408" r="40" fill="url(#thumbTone)"/>
      </g>
    </svg>
    <div class="brand" style="left:40px;top:26px;"><span class="brand-dot"></span>Brightvale</div>
    <div class="cover-title" style="top:500px;">
      <h1>COMMERCIAL CLEANING SERVICES</h1>
      <p>The Complete Cleaning Solution</p>
    </div>
    <div class="phone-pill" style="left:160px;top:574px;">
      <span class="phone-icon"><svg width="12" height="12" viewBox="0 0 24 24"><path d="M6.6 10.8a15 15 0 0 0 6.6 6.6l2.2-2.2a1 1 0 0 1 1-.25 11.4 11.4 0 0 0 3.6.6 1 1 0 0 1 1 1V20a1 1 0 0 1-1 1A17 17 0 0 1 3 4a1 1 0 0 1 1-1h3.5a1 1 0 0 1 1 1 11.4 11.4 0 0 0 .6 3.6 1 1 0 0 1-.25 1z" fill="#7b7b7b"/></svg></span>
      01632 960 418
    </div>
  </section>
</div>

<!-- Outer spread: back cover + front cover -->
<div class="sheet sheet--outer-spread">
  <section class="page page--back-cover">
    <svg class="page-art" viewBox="0 0 480 679">
      <defs>
        <linearGradient id="teamTone" x1="0" y1="0" x2="0" y2="1"><stop offset="0" stop-color="#4d5a6a"/><stop offset="1" stop-color="#2a2f36"/></linearGradient>
        <linearGradient id="bandBlue2" x1="0" y1="0" x2="0" y2="1"><stop offset="0" stop-color="#33a6d7"/><stop offset="1" stop-color="#1b6fb0"/></linearGradient>
      </defs>
      <path role="img" aria-label="Photo of the cleaning team in uniform standing beside company vans" d="M0 0 L480 0 L480 170 Q240 215 0 190 Z" fill="url(#teamTone)"/>
      <path d="M0 190 Q240 215 480 170 L480 186 Q240 232 0 206 Z" fill="var(--brand-blue)"/>
      <path d="M0 548 Q240 500 480 540 L480 560 Q240 522 0 568 Z" fill="var(--light-blue)"/>
      <path d="M0 566 Q240 520 480 558 L480 679 L0 679 Z" fill="url(#bandBlue2)"/>
    </svg>
    <div class="brand" style="left:220px;top:228px;font-size:26px;"><span class="brand-dot" style="width:13px;height:13px;"></span>Brightvale</div>
    <h2 class="heading" style="left:36px;top:280px;">The complete package</h2>
    <div class="body-copy" style="left:36px;top:312px;width:410px;">
      <p>Brightvale Services Ltd is a York based commercial cleaning company with over ten years of experience. We create bespoke cleaning packages for offices, schools and retail spaces, giving every client reliable service and real value.</p>
    </div>
    <ul class="ticks" style="left:36px;top:380px;">
      <li>Value for money</li>
      <li>Bespoke packages to suit your needs</li>
      <li>Local York Cleaning Business</li>
    </ul>
    <div class="cert-badge" style="left:370px;top:440px;" role="img" aria-label="Industry membership badge"></div>
    <p class="call-to-action" style="left:70px;top:500px;">Contact us today for a free no obligation quotation</p>
    <div class="social-row" style="left:86px;top:582px;"><span></span><span></span><span></span></div>
    <div class="phone-pill" style="left:80px;top:606px;">
      <span class="phone-icon"><svg width="12" height="12" viewBox="0 0 24 24"><path d="M6.6 10.8a15 15 0 0 0 6.6 6.6l2.2-2.2a1 1 0 0 1 1-.25 11.4 11.4 0 0 0 3.6.6 1 1 0 0 1 1 1V20a1 1 0 0 1-1 1A17 17 0 0 1 3 4a1 1 0 0 1 1-1h3.5a1 1 0 0 1 1 1 11.4 11.4 0 0 0 .6 3.6 1 1 0 0 1-.25 1z" fill="#7b7b7b"/></svg></span>
      01632 960 418
    </div>
    <p class="footer-line" style="left:20px;top:650px;">info@brightvaleservices.co.uk</p>
    <p class="footer-line" style="left:265px;top:650px;">www.brightvaleservices.co.uk</p>
  </section>

  <section class="page page--front-cover">
    <svg class="page-art" viewBox="0 0 480 679">
      <defs>
        <linearGradient id="officeTone2" x1="0" y1="0" x2="0" y2="1"><stop offset="0" stop-color="#d3dde5"/><stop offset="1" stop-color="#7d8c99"/></linearGradient>
        <linearGradient id="bandBlue3" x1="0" y1="0" x2="0" y2="1"><stop offset="0" stop-color="#33a6d7"/><stop offset="1" stop-color="#1b6fb0"/></linearGradient>
        <radialGradient id="thumbTone2"><stop offset="0" stop-color="#efe7da"/><stop offset="1" stop-color="#a99f90"/></radialGradient>
      </defs>
      <path role="img" aria-label="Photo of a bright empty open-plan office with large windows" d="M0 90 L480 90 L480 420 Q240 470 0 400 Z" fill="url(#officeTone2)"/>
      <path d="M0 400 Q240 470 480 420 L480 445 Q240 492 0 428 Z" fill="#fff"/>
      <path d="M0 462 Q240 418 480 442 L480 466 Q240 444 0 484 Z" fill="var(--light-blue)"/>
      <path d="M0 480 Q240 440 480 462 L480 679 L0 679 Z" fill="url(#bandBlue3)"/>
      <g stroke="#fff" stroke-width="4">
        <circle role="img" aria-label="Photo of a mop on a floor" cx="150" cy="432" r="40" fill="url(#thumbTone2)"/>
        <circle role="img" aria-label="Photo of a carpet being steam cleaned" cx="240" cy="420" r="50" fill="url(#thumbTone2)"/>
        <circle role="img" aria-label="Photo of a gloved hand wiping a surface" cx="330" cy="408" r="40" fill="url(#thumbTone2)"/>
      </g>
    </svg>
    <div class="brand" style="left:150px;top:26px;"><span class="brand-dot"></span>Brightvale</div>
    <div class="cover-title" style="top:500px;">
      <h1>COMMERCIAL CLEANING SERVICES</h1>
      <p>The Complete Cleaning Solution</p>
    </div>
    <div class="phone-pill" style="left:160px;top:574px;">
      <span class="phone-icon"><svg width="12" height="12" viewBox="0 0 24 24"><path d="M6.6 10.8a15 15 0 0 0 6.6 6.6l2.2-2.2a1 1 0 0 1 1-.25 11.4 11.4 0 0 0 3.6.6 1 1 0 0 1 1 1V20a1 1 0 0 1-1 1A17 17 0 0 1 3 4a1 1 0 0 1 1-1h3.5a1 1 0 0 1 1 1 11.4 11.4 0 0 0 .6 3.6 1 1 0 0 1-.25 1z" fill="#7b7b7b"/></svg></span>
      01632 960 418
    </div>
  </section>
</div>

<!-- Inner spread: commercial cleaning + carpet & oven cleaning -->
<div class="sheet sheet--inner-spread">
  <section class="page page--commercial">
    <svg class="page-art" viewBox="0 0 480 679">
      <defs>
        <linearGradient id="lobbyTone" x1="0" y1="0" x2="0" y2="1"><stop offset="0" stop-color="#eef2f5"/><stop offset="1" stop-color="#8a96a0"/></linearGradient>
        <linearGradient id="bandBlue4" x1="0" y1="0" x2="0" y2="1"><stop offset="0" stop-color="#33a6d7"/><stop offset="1" stop-color="#1b6fb0"/></linearGradient>
      </defs>
      <path role="img" aria-label="Photo of a cleaner with a trolley in a glass-walled lobby" d="M0 0 L480 0 L480 210 Q240 270 0 220 Z" fill="url(#lobbyTone)"/>
      <path d="M0 220 Q240 270 480 210 L480 226 Q240 288 0 236 Z" fill="var(--brand-blue)"/>
      <path d="M0 612 Q240 580 480 630 L480 645 Q240 598 0 628 Z" fill="var(--light-blue)"/>
      <path d="M0 626 Q240 596 480 643 L480 679 L0 679 Z" fill="url(#bandBlue4)"/>
    </svg>
    <h2 class="heading" style="left:30px;top:270px;">Commercial Cleaning in York</h2>
    <div class="body-copy" style="left:30px;top:302px;width:420px;">
      <p>We create bespoke packages to suit each individual business's needs. Whether you require cleaning daily, weekly or monthly, we are happy to create a bespoke package for you.</p>
      <p>Our team constantly strives to be the most efficient and effective commercial cleaning service in York, looking after clients from small offices to large businesses.</p>
      <p>We understand that the size of the business alone does not define the cleaning required, so we carry out a full audit of the premises before starting the contract.</p>
    </div>
    <div class="brand" style="left:300px;top:476px;font-size:24px;"><span class="brand-dot" style="width:12px;height:12px;"></span>Brightvale</div>
    <ul class="ticks" style="left:30px;top:530px;">
      <li>Hassle free contract transfer (TUPE)</li>
      <li>Value for money</li>
      <li>Bespoke packages</li>
    </ul>
  </section>

  <section class="page page--carpet-oven">
    <svg class="page-art" viewBox="0 0 480 679">
      <defs>
        <linearGradient id="carpetTone" x1="0" y1="0" x2="0" y2="1"><stop offset="0" stop-color="#9aa0ad"/><stop offset="1" stop-color="#5e6573"/></linearGradient>
        <linearGradient id="bandBlue5" x1="0" y1="0" x2="0" y2="1"><stop offset="0" stop-color="#33a6d7"/><stop offset="1" stop-color="#1b6fb0"/></linearGradient>
      </defs>
      <path role="img" aria-label="Photo of a carpet being cleaned with an extraction wand" d="M0 0 L480 0 L480 180 Q240 150 0 200 Z" fill="url(#carpetTone)"/>
      <path d="M0 200 Q240 150 480 180 L480 196 Q240 168 0 216 Z" fill="var(--brand-blue)"/>
      <path d="M0 608 Q240 574 480 590 L480 606 Q240 592 0 624 Z" fill="var(--light-blue)"/>
      <path d="M0 622 Q240 590 480 604 L480 679 L0 679 Z" fill="url(#bandBlue5)"/>
    </svg>
    <h2 class="heading" style="left:40px;top:226px;">Commercial Carpet Cleaning<span class="subheading">Putting a spring back in your step.</span></h2>
    <div class="body-copy" style="left:40px;top:276px;width:410px;">
      <p>Whether it is a bar, pub, restaurant, cinema, office or school, we have the expertise to ensure your carpets are correctly cleaned.</p>
      <p>Our professional and affordable carpet cleaning service uses tailored techniques so carpets return to pristine condition with no shrinkage and fast drying time.</p>
    </div>
    <ul class="ticks" style="left:40px;top:372px;">
      <li>Zero Shrinkage</li>
      <li>Fast drying time</li>
      <li>Increases life of carpets</li>
    </ul>
    <div class="before-after" style="left:378px;top:380px;" role="img" aria-label="Photo of a dirty oven interior before cleaning"></div>
    <div class="before-after" style="left:378px;top:452px;background:linear-gradient(160deg,#8a8a8a,#3c3c3c);" role="img" aria-label="Photo of a clean oven interior after cleaning"></div>
    <h2 class="heading" style="left:40px;top:476px;">Oven Cleaning<span class="subheading">In partnership with OvenCare Direct.</span></h2>
    <div class="body-copy" style="left:40px;top:526px;width:330px;">
      <p>Tenants, landlords and agents alike.</p>
      <p>Leading oven cleaning and repair specialists. Have your oven cleaned from as little as £45.00 (inc. VAT).</p>
    </div>
    <p class="footer-line" style="left:120px;top:620px;font-style:italic;">Contact us today for a free no obligation quotation.</p>
    <div class="phone-pill" style="left:160px;top:640px;">
      <span class="phone-icon"><svg width="12" height="12" viewBox="0 0 24 24"><path d="M6.6 10.8a15 15 0 0 0 6.6 6.6l2.2-2.2a1 1 0 0 1 1-.25 11.4 11.4 0 0 0 3.6.6 1 1 0 0 1 1 1V20a1 1 0 0 1-1 1A17 17 0 0 1 3 4a1 1 0 0 1 1-1h3.5a1 1 0 0 1 1 1 11.4 11.4 0 0 0 .6 3.6 1 1 0 0 1-.25 1z" fill="#7b7b7b"/></svg></span>
      01632 960 418
    </div>
  </section>
</div>

</body>
</html>
```